Music Festival Business Cards

The Lanternmoor Festival
Produced by Bramblewick Sound Group LLC
New music festival in Arkansas.

Target Market(s)

18-35 year olds

Industry/Entity Type

Festival

Contact Information for Business Card

We are a 5-partner team producing a music festival in Arkansas. We need slick business cards, and I want them to be square.

Requirements
Must have
• I NEED THESE TO BE IN SQUARE SIZE - 2x2 or 2.5x2.5... please not regular size.
• I need www.thelanternmoor.live as the link to website.

```html
<!DOCTYPE html>
<html lang="en">
<head>
<meta charset="utf-8">
<title>The Lanternmoor – Business Cards</title>
<link rel="stylesheet" href="https://fonts.googleapis.com/css2?family=Saira:wght@700&family=Work+Sans:wght@400&display=swap">
<style>
  :root {
    --backdrop: #1f2022;
    --card: #141516;
    --card-edge: #2a2b2d;
    --teal: #3fc4cf;
    --ink: #e6e8ea;
    --rule: #d9dbdd;
  }
  * { margin: 0; padding: 0; box-sizing: border-box; }
  html, body {
    width: 1200px;
    height: 900px;
    overflow: hidden;
    background: var(--backdrop);
  }
  .canvas {
    position: relative;
    width: 1200px;
    height: 900px;
  }
  .card {
    position: absolute;
    top: 180px;
    width: 540px;
    height: 540px;
    background: linear-gradient(135deg, #171819 0%, var(--card) 55%, #1c1d1f 100%);
    border: 1px solid var(--card-edge);
    box-shadow: 0 14px 30px rgba(0,0,0,0.45);
  }
  .card-back { left: 40px; }
  .card-front {
    left: 620px;
    display: flex;
    align-items: center;
  }

  .brand-name {
    font-family: "Saira", sans-serif;
    font-weight: 700;
    color: var(--teal);
    text-transform: uppercase;
    letter-spacing: 0.06em;
    line-height: 1.1;
  }
  .card-back .brand-name {
    position: absolute;
    top: 50%;
    left: 0;
    width: 100%;
    transform: translateY(-50%);
    text-align: center;
    font-size: 40px;
  }

  .front-brand {
    width: 262px;
    flex: none;
    display: flex;
    flex-direction: column;
    align-items: center;
    gap: 18px;
  }
  .front-brand .brand-dot {
    width: 18px;
    height: 18px;
    border-radius: 50%;
    background: var(--teal);
  }
  .front-brand .brand-name { font-size: 26px; text-align: center; }

  .divider {
    flex: none;
    width: 2px;
    height: 200px;
    background: var(--rule);
  }

  .contact {
    padding-left: 26px;
    font-family: "Work Sans", sans-serif;
    color: var(--ink);
  }
  .contact .person-name {
    font-family: "Saira", sans-serif;
    font-weight: 700;
    font-size: 25px;
    letter-spacing: 0.05em;
    color: var(--teal);
    text-transform: uppercase;
    line-height: 1;
  }
  .contact .person-role {
    font-size: 14px;
    margin-top: 4px;
    margin-bottom: 16px;
  }
  .contact .address {
    font-size: 14px;
    line-height: 1.4;
    margin-bottom: 8px;
    font-style: normal;
  }
  .contact-list { list-style: none; }
  .contact-list li {
    display: flex;
    align-items: center;
    gap: 10px;
    font-size: 14px;
    line-height: 1.6;
    white-space: nowrap;
  }
  .contact-list svg {
    width: 12px;
    height: 12px;
    flex: none;
    stroke: var(--teal);
    fill: none;
    stroke-width: 1.6;
  }
</style>
</head>
<body>
<main class="canvas">

  <section class="card card-back" aria-label="Card back">
    <p class="brand-name">The Lanternmoor</p>
  </section>

  <section class="card card-front" aria-label="Card front">
    <div class="front-brand">
      <span class="brand-dot"></span>
      <p class="brand-name">The<br>Lanternmoor</p>
    </div>

    <span class="divider"></span>

    <div class="contact">
      <h1 class="person-name">Rowan Hale</h1>
      <p class="person-role">Director</p>
      <address class="address">410 Alder Hollow Road<br>Fayetteville, AR 72701</address>
      <ul class="contact-list">
        <li>
          <svg viewBox="0 0 12 12" aria-hidden="true"><path d="M2.5 1.5 L4.5 1.5 L5.2 4 L4 5 Q5 7.2 7 8 L8 6.8 L10.5 7.5 L10.5 9.5 Q10 10.8 8.5 10.5 Q3 9 1.5 3.5 Q1.2 2 2.5 1.5 Z"/></svg>
          479 555 0182
        </li>
        <li>
          <svg viewBox="0 0 12 12" aria-hidden="true"><rect x="1" y="2.5" width="10" height="7"/><path d="M1 2.5 L6 6.5 L11 2.5"/></svg>
          info@thelanternmoor.live
        </li>
        <li>
          <svg viewBox="0 0 12 12" aria-hidden="true"><circle cx="6" cy="6" r="5"/><ellipse cx="6" cy="6" rx="2.2" ry="5"/><path d="M1 6 H11"/></svg>
          www.thelanternmoor.live
        </li>
      </ul>
    </div>
  </section>

</main>
</body>
</html>
```